Velvet Lantern Takeaway

we are emergent restaurant, serving high end of vietnamese cuisine.

Takeaway flyer's purpose must catch people attention by visual and clear dishes's description.

Please use attached logo.
And some other design for inspiration.
Updates

FLYER SIZE: DL FOLDED A4- DOUBLED SIZE. I WILL PRINT IT IN FULL COLOR AND 150GSM STOCK PAPER GLOSSTHANKS ALLHOPE I WILL GET A GREAT ONE FROM YOUKAIREN Added Tuesday, February 17, 2015

Please use images of "Vietnamese Beef Noodle PHO" if you intent to use images in the flyer Added Wednesday, February 18, 2015

Industry/Entity Type

Restaurant

Requirements
Must have
• Restaurant logo
Nice to have
• Font is very important.

```html
<!DOCTYPE html>
<html lang="en">
<head>
<meta charset="utf-8">
<title>Velvet Lantern Takeaway – Take Away Menu</title>
<link rel="stylesheet" href="https://fonts.googleapis.com/css2?family=Courier+Prime:wght@400;700&family=Oswald:wght@500;600;700&family=Bebas+Neue&family=Alfa+Slab+One&display=swap">
<style>
  :root{
    --mint:#cfe7e6;
    --mint-deep:#b9dcdb;
    --teal:#1d8c93;
    --teal-dark:#14707a;
    --aqua:#5cc6c4;
    --aqua-bright:#66d7d1;
    --orange:#e8622c;
    --orange-soft:#ee8a5a;
    --ink:#161616;
    --white:#ffffff;
    --wood:#dde4e4;
  }
  *{box-sizing:border-box;margin:0;padding:0}
  html,body{width:1200px;height:848px;overflow:hidden;background:#fff}
  .flyer{position:relative;width:1200px;height:848px;display:flex;overflow:hidden}

  /* ---------- left panel: menu ---------- */
  .menu-panel{
    width:400px;height:848px;padding:18px 14px 0 14px;
    background:radial-gradient(ellipse at 40% 40%,#d9eeec 0%,var(--mint) 55%,var(--mint-deep) 100%);
    font-family:"Courier Prime",monospace;
  }
  .menu-title{
    display:flex;align-items:center;justify-content:center;gap:10px;
    color:var(--teal);font-weight:700;font-size:20px;letter-spacing:.5px;margin:0 0 10px -10px;
  }
  .menu-title::before,.menu-title::after{content:"";width:36px;height:2px;background:var(--teal)}
  .dish{margin-bottom:2px}
  .dish-name,.dish-row{font-size:13.4px;font-weight:700;color:var(--ink);line-height:17.5px}
  .dish-row{display:flex;align-items:baseline}
  .dots{flex:1;border-bottom:2px dotted var(--ink);margin:0 6px 3px}
  .price{min-width:40px;text-align:right}
  .pick{display:inline-block;width:10px;height:10px;border-radius:50%;background:var(--orange);margin-left:4px;vertical-align:0}
  .dish-desc{font-size:10.6px;color:var(--orange);font-weight:700;line-height:12.4px;margin-bottom:2px}

  /* ---------- middle panel: delivery ---------- */
  .info-panel{
    width:395px;height:848px;position:relative;
    background:radial-gradient(ellipse at 50% 45%,#d3ebe9 0%,#bfe0de 60%,#a9d3d1 100%);
    text-align:center;
  }
  .tagline{position:absolute;left:22px;top:52px;display:flex;gap:10px;font-family:"Oswald",sans-serif;font-weight:700}
  .tagline-the{writing-mode:vertical-rl;transform:rotate(180deg);color:var(--teal);font-size:32px;line-height:30px;letter-spacing:1px}
  .tagline-lines{text-align:left;line-height:32px}
  .tagline-lines .white{color:var(--white);font-size:32px}
  .tagline-lines .teal{color:var(--teal);font-size:24px}
  .delivery-title{position:absolute;top:256px;left:0;right:0;font-family:"Oswald",sans-serif;font-weight:600;font-size:27px;color:var(--teal);letter-spacing:1.5px}
  .suburbs{
    position:absolute;top:305px;left:10px;width:380px;
    font-family:"Alfa Slab One",serif;font-size:16.5px;line-height:23px;color:var(--white);
    transform:rotate(-6deg);
  }
  .divider-ornament{position:absolute;left:170px;width:54px;height:22px;background:var(--orange-soft);border-radius:50% 50% 6px 6px}
  .rule{position:absolute;left:52px;width:290px;height:2px;background:var(--orange-soft)}
  .order-info{position:absolute;top:538px;left:0;right:0;font-family:"Courier Prime",monospace;color:var(--teal);font-weight:700}
  .order-info .small{font-size:15px;line-height:20px;font-weight:400}
  .order-info .mid{font-size:21px;line-height:22px}
  .order-info .big{font-family:"Oswald",sans-serif;font-size:34px;line-height:40px;letter-spacing:1px}
  .order-info .line{font-size:15.5px;line-height:21px}
  .notes{position:absolute;top:736px;left:14px;width:370px;list-style:none;font-family:"Courier Prime",monospace;font-size:12.3px;line-height:14.5px;color:var(--teal);text-align:center}
  .notes li::before{content:"• "}

  /* ---------- right panel: cover ---------- */
  .cover-panel{width:405px;height:848px;position:relative;background:var(--aqua)}
  .wood{position:absolute;left:0;top:0;width:405px;height:190px;
    background:repeating-linear-gradient(180deg,#e6ecec 0 44px,#cfd8d9 44px 47px),var(--wood)}
  .brand{position:absolute;top:12px;left:0;width:405px;text-align:center;color:var(--teal)}
  .brand-mark{display:inline-block;width:12px;height:12px;background:var(--orange-soft);margin-right:8px;vertical-align:middle}
  .brand-name{font-family:"Bebas Neue",sans-serif;font-size:58px;line-height:56px;letter-spacing:1px}
  .brand-sub{font-family:"Oswald",sans-serif;font-size:11px;letter-spacing:3px;color:var(--orange)}
  .brand-phone{font-family:"Oswald",sans-serif;font-weight:600;font-size:22px;color:var(--orange-soft);margin-top:20px;letter-spacing:1px}
  .brand-phone small{font-size:11px}
  .torn{position:absolute;left:0;top:208px;width:405px;height:240px;background:#8fd9d6;clip-path:polygon(0 12%,30% 4%,62% 10%,100% 0,100% 90%,70% 96%,40% 88%,0 100%)}
  .lotus-spot{position:absolute;background:rgba(255,255,255,.55);border-radius:50% 50% 8px 8px}
  .takeaway{position:absolute;top:258px;left:208px;font-family:"Bebas Neue",sans-serif;font-size:42px;line-height:36px;color:var(--white);text-shadow:2px 2px 0 #3a3a3a;transform:rotate(-8deg);text-align:center}
  .menu-word{position:absolute;top:325px;left:86px;font-family:"Bebas Neue",sans-serif;font-size:100px;line-height:90px;color:var(--aqua-bright);text-shadow:3px 3px 0 #2c6f73;transform:rotate(-6deg)}
  .slogan{position:absolute;top:492px;left:26px;width:360px;font-family:"Bebas Neue",sans-serif;color:var(--white)}
  .slogan .s1{font-size:44px;line-height:42px;letter-spacing:1px}
  .slogan .s2{font-size:118px;line-height:96px;letter-spacing:2px}
  .slogan .s3{font-size:42px;line-height:80px}
  .slogan .s3 b{font-weight:400;font-size:86px;color:var(--teal)}
  .slogan .s4{font-size:42px;line-height:40px;display:flex;align-items:center;gap:10px}
  .slogan .s4 span{background:var(--white);color:var(--aqua);padding:0 12px;font-size:50px;letter-spacing:2px}
  .social{position:absolute;bottom:24px;right:26px;display:flex;gap:8px}
  .social span{width:30px;height:30px;border-radius:5px}
</style>
</head>
<body>
<div class="flyer">

  <section class="menu-panel">
    <h2 class="menu-title">CHEF FAVOURITES</h2>

    <div class="dish"><div class="dish-name">Stuffed Bean Curd</div><div class="dish-row">in home made sauce<span class="dots"></span><span class="price">15.90</span></div><p class="dish-desc">Fried Bean Curd stuffed with Chicken Minces,<br>mushroom, vermicelli</p></div>
    <div class="dish"><div class="dish-name">Stir-fry Snow Pea</div><div class="dish-row">with Beef and Pineapple<span class="dots"></span><span class="price">17.90</span></div></div>
    <div class="dish"><div class="dish-row">Shaking Beef<span class="pick"></span><span class="dots"></span><span class="price">17.90</span></div><p class="dish-desc">Beef wok-tossed with oyster sauce &amp; black pepper</p></div>
    <div class="dish"><div class="dish-name">Vietnamese Style stir-fry Beef</div><div class="dish-row">with Fusilli Pasta<span class="dots"></span><span class="price">8.50</span></div></div>
    <div class="dish"><div class="dish-name">Caramelized Chicken</div><div class="dish-row">with coconut juice<span class="dots"></span><span class="price">17.90</span></div></div>
    <div class="dish"><div class="dish-row">Lemongrass Chilli Chicken (HOT)<span class="pick"></span><span class="dots"></span><span class="price">17.90</span></div><p class="dish-desc">Stir-fry lemongrass &amp; chilli caramel chicken<br>with crushed cashew nuts</p></div>
    <div class="dish"><div class="dish-row">Stuffed boneless Chicken wings<span class="dots"></span><span class="price">18.90</span></div><p class="dish-desc">Boneless chickens stuffed with pork mince,<br>mushroom, shallot &amp; fried until golden brown<br>served with special tamarind sauce</p></div>
    <div class="dish"><div class="dish-row">Char-grilled Honey Chicken GF<span class="pick"></span><span class="dots"></span><span class="price">18.90</span></div><p class="dish-desc">Char-grilled honey marinated chicken<br>with a green salad</p></div>
    <div class="dish"><div class="dish-name">Traditional Vietnamese</div><div class="dish-row">Fried Fish Sauce Chicken (HOT)<span class="dots"></span><span class="price">17.90</span></div><p class="dish-desc">Fried chicken in secret fish sauce<br>with crushed chilli</p></div>
    <div class="dish"><div class="dish-row">Five Spices Chicken<span class="dots"></span><span class="price">16.90</span></div><p class="dish-desc">Slow cooked five spices chicken served with pickles</p></div>
    <div class="dish"><div class="dish-name">Stir-fry Lemongrass Lean Pork</div><div class="dish-row">with mix vegetables<span class="pick"></span><span class="dots"></span><span class="price">16.90</span></div></div>
    <div class="dish"><div class="dish-name">Pork Belly Braised</div><div class="dish-row">in Coconut Juice<span class="dots"></span><span class="price">16.90</span></div><p class="dish-desc">Tasty braised caramelised pork belly &amp; eggs</p></div>
    <div class="dish"><div class="dish-row">Lean Pork and Prawn wok tossed<span class="dots"></span><span class="price">16.90</span></div></div>
    <div class="dish"><div class="dish-name">Saigon Iconic Chargrilled Pork Chops</div><div class="dish-row">with Rice<span class="dots"></span><span class="price">17.90</span></div></div>
    <div class="dish"><div class="dish-row">Clay pot Fish GF<span class="dots"></span><span class="price">20.50</span></div><p class="dish-desc">Caramelised Fish fillet in garlic fish sauce &amp; pepper</p></div>
    <div class="dish"><div class="dish-name">Pan-fried marinated Barramundi</div><div class="dish-row">crushed in lemongrass<span class="dots"></span><span class="price">20.50</span></div></div>
    <div class="dish"><div class="dish-row">Mekong Signature GF<span class="dots"></span><span class="price">20.50</span></div><p class="dish-desc">Tiger prawns wok tossed in coconut cream</p></div>
    <div class="dish"><div class="dish-row">Salt and pepper Prawn<span class="dots"></span><span class="price">20.50</span></div><p class="dish-desc">Lightly battered pepper salted Tiger Prawn</p></div>
    <div class="dish"><div class="dish-row">Stir-fry Combination Seafood<span class="pick"></span><span class="dots"></span><span class="price">20.50</span></div><p class="dish-desc">Prawns, squids, fish with broccoli,<br>snow peas &amp; carrots</p></div>
  </section>

  <section class="info-panel">
    <div class="tagline">
      <div class="tagline-the">THE</div>
      <div class="tagline-lines">
        <div class="white">TRUE TASTE</div>
        <div><span class="white">OF SAIGON</span> <span class="teal">FROM</span></div>
        <div class="teal">STREETS OF VIETNAM</div>
      </div>
    </div>

    <h3 class="delivery-title">DELIVERY SUBURBS</h3>
    <p class="suburbs">Cammeray, Cremorne, Crows Nest, Greenwich, Kirribilli, Lavender Bay, Mcmahons Point, Milsons Point, Naremburn, Neutral Bay, North Sydney, St Leonards, Waverton &amp; Wollstonecraft</p>

    <div class="divider-ornament" style="top:503px" role="img" aria-label="Small lotus ornament"></div>
    <div class="rule" style="top:529px"></div>
    <div class="order-info">
      <div class="small">Free Home Delivery Orders via</div>
      <div class="mid">TEXT MESSAGES ONLY</div>
      <div class="big">0400 555 273</div>
      <div class="line">Minimum Order $25.</div>
      <div class="line">EFTPOS Payment is Available</div>
      <div class="line">5.30 – 9.45 pm 7NIGHTS</div>
    </div>
    <div class="rule" style="top:686px"></div>
    <div class="divider-ornament" style="top:698px" role="img" aria-label="Small lotus ornament"></div>

    <ul class="notes">
      <li>Food ingredients and prices are subject to be changed without prior notice</li>
      <li>If you have any special dietary requirements or food allergies please notify us prior to ordering. We are unable to guarantee any of our dishes to be allergen free</li>
    </ul>
  </section>

  <section class="cover-panel">
    <div class="wood" role="img" aria-label="Weathered white painted wood planks"></div>
    <div class="brand">
      <div class="brand-name"><span class="brand-mark"></span>VELVET LANTERN</div>
      <div class="brand-sub">NORTH SYDNEY · EST. 2014</div>
      <div class="brand-phone"><small>PH.:</small> (02) 9000 4187</div>
    </div>

    <div class="torn" role="img" aria-label="Torn paper strip in pale aqua"></div>
    <div class="lotus-spot" style="left:80px;top:278px;width:80px;height:52px" role="img" aria-label="Outlined lotus flower decoration"></div>
    <div class="takeaway">TAKE<br>AWAY</div>
    <div class="menu-word">MENU</div>

    <div class="slogan">
      <div class="s1">BRINGING THE</div>
      <div class="s2">TASTE</div>
      <div class="s3">OF <b>SAIGON</b></div>
      <div class="s4">TO <span>SYDNEY</span></div>
    </div>

    <div class="social" aria-label="Social media links">
      <span style="background:#3b5b99"></span>
      <span style="background:#3ba9e0"></span>
      <span style="background:#d9483b"></span>
      <span style="background:#5a7fa3"></span>
      <span style="background:#cc2233"></span>
    </div>
  </section>

</div>
</body>
</html>
```